Water Damage? Call Us!!

We are an established water damage mitigation company opening a storm chasing division. We will need the flyer to express urgency to call for water damage structural drying and demolition. I have attached our logo in various formats.

Check out our website for some ideas of what we do. www.parklinerestoration.com

Include:

Parkline Restoration, LLC
Office@ParklineRestoration.com
www.parklinerestoration.com
877-HELP-NOW
877-435-7669

I don't want to have our locations on there.

Target Market(s)

When someone has water damage to their home or business, we remove the wet material and then use fans and dehumidifiers to remove the moisture from the structure. We are like a Kelvora, but better. Lol

Colors

Designer to choose colors to be used in the design.

Requirements
Must have
• I have included various certification logos to use.
• Water damage must be the main focal point.
• We need to call them to action by calling us to dry their property. We will be dropping these flyers off in damaged areas.
• Trained in Drying Science by the NBRTA
• We handle Residential, Commercial, Hotels, Multi-Family.
• We specialize in Insurance Claims.
• We can bill your insurance company directly.
• Our Services include:
• Water Extraction/Muck Out
• Deconstruction of Damaged Materials
• Structural Drying
• Anti-Microbial Application
• Roofing
Nice to have
• It would be nice to have some thermal images of wet areas
Should not have
• Not looking for a fun flyer. These potential clients have suffered from devastation and we are looking to help them by getting their home or business back to normal.

```html
<!DOCTYPE html>
<html lang="en">
<head>
<meta charset="utf-8">
<title>Parkline Restoration – Water Damage Flyer</title>
<link rel="stylesheet" href="https://fonts.googleapis.com/css2?family=Montserrat:wght@300;400;600;700;800&family=Oswald:wght@500&display=swap">
<style>
  :root{
    --red:#ea4140;
    --ink:#2a2a2a;
    --body:#555;
    --navy:#2b2f8f;
    --paper:#ffffff;
    --panel:#f1f1f1;
    --backdrop:#a9a9ab;
    --yellow:#f7c81e;
    --rule:#cfcfcf;
  }
  *{box-sizing:border-box;margin:0;padding:0}
  html,body{width:1200px;height:1200px;overflow:hidden;background:var(--backdrop)}
  body{font-family:"Montserrat",Arial,sans-serif;position:relative}
  .flyer{position:absolute;left:160px;top:30px;width:880px;height:1140px;background:var(--paper);overflow:hidden;box-shadow:0 6px 24px rgba(0,0,0,.18)}

  .hero-photo{position:absolute;left:250px;top:0;width:630px;height:570px;
    background:linear-gradient(160deg,#ecebe8 0%,#d9d6d1 35%,#8a6a58 60%,#a8744a 100%)}

  .tagline{position:absolute;left:520px;top:38px;width:330px;height:42px;background:#fff;
    font-size:15px;letter-spacing:4px;color:#555;display:flex;align-items:center;padding-left:26px;z-index:2}
  .tagline-tab{position:absolute;left:850px;top:38px;width:30px;height:42px;background:var(--red);z-index:2}

  .brand{position:absolute;left:0;top:0;width:250px;height:230px;background:#fff;display:flex;align-items:center;justify-content:center;gap:10px;padding:0 18px}
  .brand-mark{width:22px;height:22px;border-radius:50%;background:var(--red);flex:none}
  .brand-name{font-weight:800;font-size:21px;line-height:1.15;color:var(--red)}

  .headline-block{position:absolute;left:0;top:300px;width:420px;height:250px;background:var(--red);color:#fff;padding:36px 0 0 40px;z-index:2}
  .headline-kicker{font-weight:300;font-size:30px;letter-spacing:4px}
  .headline{font-weight:700;font-size:30px;letter-spacing:4px;line-height:1.3;margin-top:2px}

  .phone-bar{position:absolute;left:600px;top:440px;width:280px;height:72px;background:var(--red);display:flex;align-items:center;padding-left:78px;
    font-family:"Oswald",Arial,sans-serif;font-weight:500;font-size:32px;color:#fff;letter-spacing:1px;z-index:2}
  .phone-badge{position:absolute;left:568px;top:444px;width:64px;height:64px;z-index:3}

  .seal{position:absolute;left:420px;top:420px;width:140px;height:140px;z-index:3}

  .contact-panel{position:absolute;left:390px;top:570px;width:490px;height:570px;background:var(--panel)}

  .about{position:absolute;left:430px;top:592px;width:420px}
  .section-title{color:var(--red);font-weight:700;font-size:17px;letter-spacing:1.5px}
  .about p{font-size:13px;color:var(--body);line-height:1.45;margin-top:8px}
  .facts{list-style:none;margin-top:12px;font-size:14px;color:var(--ink);line-height:1.5}
  .facts b{font-weight:700}

  .services-title{color:var(--red);font-weight:700;font-size:17px;letter-spacing:1.5px;margin-top:10px}
  .services{list-style:none;margin-top:8px}
  .services li{display:flex;align-items:center;gap:18px;height:34px;color:var(--navy);font-weight:600;font-size:14px}
  .services svg{width:26px;height:26px;flex:none}

  .contact-rule{position:absolute;left:430px;top:1024px;width:420px;border-top:1px solid var(--rule)}
  .contact-web{position:absolute;left:640px;top:1034px;font-size:12.5px;color:#444;line-height:1.6}
  .contact-phone{position:absolute;left:430px;top:1088px;font-size:12.5px;color:#444;line-height:1.6}
  .contact-web b,.contact-phone b{font-weight:700}

  .certs{position:absolute;left:40px;top:610px;width:330px}
  .cert-grid{display:grid;grid-template-columns:1fr 1fr;gap:26px 28px;margin-top:24px}
  .cert{height:96px;display:flex;align-items:center;justify-content:center}

  .get-in-touch{position:absolute;left:40px;top:1060px}
  .get-in-touch .company{font-size:16px;color:#555;margin-top:6px;letter-spacing:.5px}
</style>
</head>
<body>
<main class="flyer">

  <div class="hero-photo" role="img" aria-label="Photo: hand holding a thermal imaging camera showing moisture on the floor of a bright empty room"></div>

  <div class="tagline">STOP IT BEFORE IT STARTS</div>
  <div class="tagline-tab"></div>

  <div class="brand">
    <span class="brand-mark"></span>
    <span class="brand-name">Parkline Restoration</span>
  </div>

  <section class="headline-block">
    <div class="headline-kicker">RESTORE</div>
    <h1 class="headline">WATER DAMAGED<br>STRUCTURES<br>&amp; PROPERTIES</h1>
  </section>

  <div class="phone-bar">877-HELP-NOW</div>
  <svg class="phone-badge" viewBox="0 0 64 64" aria-hidden="true">
    <circle cx="32" cy="32" r="31" fill="var(--yellow)"/>
    <circle cx="32" cy="32" r="24" fill="#e8e8e8"/>
    <path d="M22 20c2-2 5-2 6 0l3 5c1 2 0 3-1 4l-2 2c2 4 5 7 9 9l2-2c1-1 2-2 4-1l5 3c2 1 2 4 0 6-3 3-7 4-12 1-7-4-12-9-16-16-2-5-1-9 2-11z" fill="#222"/>
  </svg>

  <svg class="seal" viewBox="0 0 150 150" role="img" aria-label="Certified inspector seal">
    <circle cx="75" cy="75" r="73" fill="#8f8672"/>
    <circle cx="75" cy="75" r="64" fill="#d9d2bd"/>
    <circle cx="75" cy="75" r="44" fill="#b7ad93"/>
  </svg>

  <div class="contact-panel"></div>

  <section class="about">
    <h2 class="section-title">ABOUT US</h2>
    <p>Parkline Restoration is uniquely positioned to be one of the leading water damage restoration companies in the state.</p>
    <ul class="facts">
      <li>- <b>NBRTA</b> Certified</li>
      <li>- <b>24*7</b> Available</li>
      <li>- <b>60 minutes</b> turn around time</li>
      <li>- <b>Bill directly</b> to insurance company</li>
      <li>- <b>Family</b> Owned &amp; Operated</li>
      <li>- <b>Residential &amp; Commercial</b> projects expertise</li>
    </ul>
    <h2 class="services-title">Our Services include:</h2>
    <ul class="services">
      <li><svg viewBox="0 0 28 28" aria-hidden="true"><rect x="4" y="9" width="18" height="12" rx="2" fill="none" stroke="#222" stroke-width="1.6"/><path d="M22 13h3v4h-3M8 9V6h8v3M13 12l-2 4h4l-2 4" fill="none" stroke="#222" stroke-width="1.6"/></svg>Water Extraction/Muck Out</li>
      <li><svg viewBox="0 0 28 28" aria-hidden="true"><rect x="3" y="10" width="12" height="7" rx="3.5" fill="none" stroke="#222" stroke-width="1.8" transform="rotate(-25 9 13)"/><rect x="13" y="12" width="12" height="7" rx="3.5" fill="none" stroke="#222" stroke-width="1.8" transform="rotate(-25 19 15)"/></svg>Deconstruction of Damaged Materials</li>
      <li><svg viewBox="0 0 28 28" aria-hidden="true"><path d="M14 3c4 6 7 10 7 14a7 7 0 0 1-14 0c0-4 3-8 7-14z" fill="none" stroke="#222" stroke-width="1.6"/><path d="M6 25L22 3" stroke="#222" stroke-width="1.6"/></svg>Structural Drying</li>
      <li><svg viewBox="0 0 28 28" aria-hidden="true"><circle cx="14" cy="14" r="6" fill="none" stroke="#222" stroke-width="1.6"/><path d="M14 2v6M14 20v6M2 14h6M20 14h6M6 6l4 4M18 18l4 4M22 6l-4 4M10 18l-4 4" stroke="#222" stroke-width="1.6"/></svg>Anti-Microbial Application</li>
      <li><svg viewBox="0 0 28 28" aria-hidden="true"><path d="M6 8h18l-3 14H3z" fill="none" stroke="#222" stroke-width="1.6"/><path d="M11 8L8 22M17 8l-3 14M5 13h18M4 18h18" stroke="#222" stroke-width="1.2"/></svg>Roofing</li>
    </ul>
  </section>

  <div class="contact-rule"></div>
  <div class="contact-web"><b>E:</b> Office@ParklineRestoration.com<br><b>W:</b> www.parklinerestoration.com</div>
  <div class="contact-phone"><b>T</b> : 877-HELP-NOW<br><b>M</b> : 877-435-7669</div>

  <section class="certs">
    <h2 class="section-title">CERTIFICATIONS</h2>
    <div class="cert-grid">
      <div class="cert"><svg width="130" height="90" viewBox="0 0 130 90" role="img" aria-label="Commercial inspector certification badge"><rect x="10" y="20" width="110" height="50" rx="6" fill="#c6993d"/></svg></div>
      <div class="cert"><svg width="90" height="90" viewBox="0 0 90 90" role="img" aria-label="Infrared certification badge"><circle cx="45" cy="45" r="38" fill="none" stroke="#3aa0d8" stroke-width="10"/></svg></div>
      <div class="cert"><svg width="130" height="96" viewBox="0 0 130 96" role="img" aria-label="Residential property inspector certification badge"><rect x="12" y="18" width="106" height="60" rx="8" fill="#2c3a57"/></svg></div>
      <div class="cert"><svg width="130" height="80" viewBox="0 0 130 80" role="img" aria-label="Roof inspector certification badge"><rect x="10" y="14" width="110" height="52" rx="4" fill="#4a4a4a"/></svg></div>
      <div class="cert"><svg width="110" height="100" viewBox="0 0 110 100" role="img" aria-label="Moisture intrusion inspector certification badge"><circle cx="55" cy="50" r="44" fill="#5c9a3a"/></svg></div>
      <div class="cert"><svg width="110" height="100" viewBox="0 0 110 100" role="img" aria-label="Exterior inspector certification badge"><rect x="25" y="10" width="60" height="80" rx="4" fill="#b8743c"/></svg></div>
    </div>
  </section>

  <section class="get-in-touch">
    <h2 class="section-title">GET IN TOUCH</h2>
    <div class="company">Parkline Restoration, LLC</div>
  </section>

</main>
</body>
</html>
```